Psychologist in Private Practice Needs a Website Update

Project Description:
Hello talented designers! My current website, www.junetillard.com, needs a fresh, boho-modern makeover that highlights the warm, welcoming nature of my holistic therapy practice. I want a website that has a serene, boho- modern design, appealing to clients seeking individual therapy, couples therapy, and family counseling.

I’d also like to prepare for a future second site focused exclusively on couples and family therapy. Both sites should be interconnected, so I’m looking for design suggestions that seamlessly link them together while maintaining a cohesive brand look and feel.

Key Objectives:

Boho-Modern Aesthetic: Incorporate natural textures, neutral or earthy tones, and clean lines that capture a modern, inviting vibe.

Responsive Design: Ensure the website is user-friendly on desktop, tablet, and mobile devices.

Clear Service Offerings: Prominently feature my three distinct services: individual therapy, couples therapy, and family counseling.

Interlinked Future Site: Provide ideas on how to cross-link this site with a second site focused on couples and family therapy.

User Experience (UX): Make the site simple to navigate, with intuitive placement of content that speaks to potential clients’ needs.

SEO-Friendly: Implement best practices for structure, site speed, and keyword usage to boost online visibility.

What I Have Now:
Existing website: www.junetillard.com
Basic content and a logo that can be refined or updated to match the boho-modern feel
Rough style guide with brand elements open to a fresh interpretation

Preferred Style/Tone:
Boho-modern with earthy tones, subtle textures, and clean typography
Warm, empathetic, and approachable to align with the nature of therapy services
Slightly artistic or organic elements that evoke calm and connection

Potential for an ongoing design relationship!
Updates

Need extra days to review

Target Market(s)

I have a high functioning, professional clientele who doctors, lawyers, and leaders in their field.

Industry/Entity Type

healthcare/mental health

Coding

Coded - Design and coding required

Font styles to use
Other font styles liked:
• cormorant garamond for headers and Source Sans Pro for supporting text

Colors

Designer to choose colors to be used in the design.

Requirements
Must have
• Open, Harmonious Layout I’d like the overall design to feel upscale, humanistic, open and harmonious, with minimal divisions of space. Rather than traditional section dividers, please consider using images, subtle shifts in color, typography, or spacing to define sections. Hero Image & Inspiration Ideally, the first (hero) image should evoke a sense of awe or inspiration. Focus on simplicity and elegance so the design feels spacious and inviting, allowing the content and imagery to really stand out. Natural Flow Wherever possible, let the design elements flow naturally into each other, creating a sense of unity and cohesion throughout the site.
Nice to have
• 1. Full-Width Hero Image: • The homepage should feature a full-width hero image that extends edge-to-edge across the screen for a modern and visually immersive effect. • This image should set the tone for the website, reflecting a calming, humanistic/natural, and upscale feel. It could include subtle overlays or gradients to enhance readability of text and navigation elements. Ideally, this image should have one or two people in nature. The image could be slightly transparent to allow the text "holistic therapy" and the tagline "an integrative approach to transformation" to be easily visible. Please help me find a breath-taking image that evokes a sense of beauty, inspiration, awe or hope. 2. Menu Tabs Positioned Over the Image: • The menu tabs (navigation bar) should be positioned directly on top of the hero image, either centered or aligned to the top right/left, depending on the design. • The navigation bar should have a slightly transparent or solid background (depending on the image and visibility needs) to ensure the text is easily readable without detracting from the image. 3. Typography and Text Placement: • The text overlay on the hero image should use the selected fonts: • Cormorant Garamond for headers (e.g., the tagline or welcome message). • Source Sans Pro for any supporting text. 5. Seamless Transitions: • Below the full-width image, transitions into the next sections (like “About,” “Services,” or client-focused content) should be smooth, using full-width separators that maintain the cohesive, open layout style. 6. Color Palette: • A neutral and calming color palette should be used (e.g., soft blues, grays, whites, or very muted earth tones) to create a soothing atmosphere for visitors. This design approach ensures the homepage looks clean, modern, and professional while maintaining the calming and upscale aesthetic that reflects the values of my psychology practice

```html
<!DOCTYPE html>
<html lang="en">
<head>
<meta charset="utf-8">
<title>Dr. June Tillard — Licensed Psychologists</title>
<link href="https://fonts.googleapis.com/css2?family=Questrial&family=Poppins:wght@400;500&family=Cormorant+Garamond:ital,wght@1,500;1,600&display=swap" rel="stylesheet">
<style>
:root{
  --sage:#5e8a6e;
  --sage-dark:#4f7a5f;
  --clay:#d8b3a1;
  --clay-deep:#c98f74;
  --blush:#f8e4da;
  --rose:#c8897a;
  --ink:#2c2a29;
  --text:#3d3a38;
  --white:#ffffff;
  --sand:#d7bfa6;
  --footer:#c68d74;
}
*{box-sizing:border-box;margin:0;padding:0}
html,body{width:1200px;height:4000px;overflow:hidden}
body{font-family:"Poppins",sans-serif;color:var(--text);background:var(--white)}
.canvas{position:relative;width:1200px;height:4000px;overflow:hidden}
.abs{position:absolute}
.heading{font-family:"Questrial",sans-serif;font-weight:400;color:var(--ink);letter-spacing:1.5px}
.eyebrow{font-family:"Cormorant Garamond",serif;font-style:italic;font-weight:600;color:var(--rose);font-size:24px}
.btn{position:absolute;display:flex;align-items:center;justify-content:center;background:var(--sage);color:var(--white);font-family:"Questrial",sans-serif;font-size:19px;letter-spacing:1px;text-decoration:none}
.photo{position:absolute}
.arch{border-radius:180px 180px 0 0}

/* nav */
.site-header{position:absolute;left:0;top:0;width:1200px;height:82px;background:var(--white)}
.brand{position:absolute;left:75px;top:8px;color:var(--sage)}
.brand-name{font-family:"Cormorant Garamond",serif;font-style:italic;font-weight:600;font-size:40px;line-height:44px;display:block}
.brand-tag{font-family:"Cormorant Garamond",serif;font-style:italic;font-weight:600;font-size:18px;display:block;margin-left:62px;margin-top:-4px}
.nav a{position:absolute;top:31px;font-family:"Questrial",sans-serif;font-size:17px;color:var(--ink);text-decoration:none}
.nav a.active{color:var(--sage);text-decoration:underline;text-underline-offset:4px}

/* hero */
.hero{position:absolute;left:0;top:82px;width:1200px;height:638px;background:var(--clay)}
.hero-title{position:absolute;left:632px;top:186px;font-size:63px;color:var(--white);letter-spacing:3px}
.hero-sub{position:absolute;left:636px;top:266px;font-size:39px;line-height:47px;color:var(--white);letter-spacing:2px}
.arrow{position:absolute;width:22px;height:30px}

/* about */
.about-name{position:absolute;left:371px;top:850px;font-size:45px}
.about-role{position:absolute;left:373px;top:906px;font-family:"Questrial",sans-serif;font-size:17px;color:var(--sage);letter-spacing:.5px}
.about-text{position:absolute;left:372px;top:948px;width:448px;font-size:13px;line-height:27.2px;color:var(--ink)}

/* services */
.services{position:absolute;left:0;top:1316px;width:1200px;height:717px;background:var(--blush)}
.card{position:absolute;top:1501px;width:329px;height:462px;background:var(--white)}
.card .photo{left:0;top:0;width:329px;height:273px}
.card h3{position:absolute;top:288px;width:100%;text-align:center;font-family:"Questrial",sans-serif;font-weight:400;font-size:23px;color:var(--rose);letter-spacing:1px}
.card p{position:absolute;top:323px;left:22px;right:22px;text-align:center;font-size:13px;line-height:24.5px;color:var(--ink)}
.card .btn{left:87px;top:410px;width:156px;height:52px}

/* issues */
.issues-title{position:absolute;left:75px;top:2088px;font-size:45px;line-height:45.5px;letter-spacing:2px}
.issues-intro{position:absolute;left:75px;top:2244px;width:690px;font-size:13px;line-height:27px;color:var(--ink)}
.checklist{position:absolute;left:75px;top:2310px;list-style:none}
.checklist li{display:flex;align-items:center;height:29.5px;font-size:13px;color:var(--ink)}
.checklist svg{width:12px;height:12px;margin-right:16px}

/* partnership */
.partnership{position:absolute;left:0;top:2641px;width:1200px;height:444px;background:linear-gradient(120deg,#d8a587 0%,#d29c7e 45%,#dcae92 100%)}
.partnership h2{position:absolute;left:0;top:98px;width:100%;text-align:center;font-size:46px;color:var(--white);letter-spacing:2px}
.partnership p{position:absolute;left:100px;top:168px;width:1000px;text-align:center;font-size:12.5px;line-height:27px;color:var(--white)}

/* blog */
.blog-title{position:absolute;left:73px;top:3130px;font-size:46px}
.post{position:absolute;top:3208px;width:329px}
.post .photo{position:relative;width:329px;height:200px}
.post h3{margin-top:24px;font-family:"Questrial",sans-serif;font-weight:400;font-size:21px;line-height:28px;color:var(--ink);letter-spacing:.5px}
.post a{display:block;margin-top:12px;font-size:13px;color:var(--rose);text-decoration:underline}

/* footer */
.site-footer{position:absolute;left:0;top:3624px;width:1200px;height:376px;background:var(--footer);color:var(--white)}
.f-col{position:absolute;top:51px}
.f-col h4{font-family:"Questrial",sans-serif;font-weight:400;font-size:21px;letter-spacing:1px;margin-bottom:9px}
.f-col a,.f-col span{display:block;font-size:13.5px;line-height:32.6px;color:var(--white);text-decoration:none}
.contact-row{display:flex;align-items:center}
.contact-row svg{width:14px;height:14px;margin-right:14px}
.email-input{position:absolute;left:885px;top:96px;width:242px;height:45px;background:var(--white);font-size:13px;color:var(--ink);padding:13px 16px}
.subscribe{left:885px;top:154px;width:242px;height:44px;font-size:18px}
.social{position:absolute;top:176px;left:593px;display:flex;gap:14px}
.social span{width:26px;height:26px;border-radius:50%;border:2px solid var(--white);display:block}
.social span.on{background:var(--sage);border-color:var(--sage)}
.f-rule{position:absolute;left:75px;top:318px;width:1052px;height:1px;background:rgba(255,255,255,.35)}
.copyright{position:absolute;left:0;top:338px;width:100%;text-align:center;font-size:13px}
</style>
</head>
<body>
<div class="canvas">

  <header class="site-header">
    <div class="brand">
      <span class="brand-name">Dr. June Tillard</span>
      <span class="brand-tag">Licensed Psychologists</span>
    </div>
    <nav class="nav">
      <a class="active" href="#" style="left:551px">Welcome</a>
      <a href="#" style="left:673px">Services</a>
      <a href="#" style="left:790px">About</a>
      <a href="#" style="left:886px">FAQs</a>
      <a href="#" style="left:979px">Blog</a>
      <a href="#" style="left:1063px">Contact</a>
    </nav>
  </header>

  <section class="hero">
    <div class="photo" role="img" aria-label="Golden pampas grass on a hazy beach" style="left:0;top:0;width:433px;height:638px;background:linear-gradient(180deg,#d9cfc4 0%,#cdb08e 55%,#b98a5e 100%)"></div>
    <div class="photo arch" role="img" aria-label="Therapist taking notes during a session with a client" style="left:264px;top:73px;width:344px;height:491px;border:4px solid #e9cbbb;background:linear-gradient(180deg,#d6d1cb 0%,#b7a08a 55%,#7d6552 100%)"></div>
    <h1 class="heading hero-title">Holistic Therapy</h1>
    <p class="heading hero-sub">An integrative approach<br>to transformation.</p>
    <a class="btn" href="#" style="left:636px;top:384px;width:156px;height:51px">Read More</a>
    <svg class="arrow" style="left:632px;top:455px" viewBox="0 0 22 30"><path d="M16 4 L6 15 L16 26" fill="none" stroke="#3d3a38" stroke-width="2"/></svg>
    <svg class="arrow" style="left:674px;top:455px" viewBox="0 0 22 30"><path d="M6 4 L16 15 L6 26" fill="none" stroke="#ffffff" stroke-width="2"/></svg>
  </section>

  <section class="about">
    <div class="photo" role="img" aria-label="Psychologist working at a laptop beside houseplants" style="left:75px;top:823px;width:268px;height:391px;background:linear-gradient(180deg,#dfe1dc 0%,#9aa393 50%,#6b5a4c 100%)"></div>
    <div class="photo" role="img" aria-label="Portrait of Dr. June Tillard standing in a bright room" style="left:855px;top:720px;width:345px;height:596px;background:linear-gradient(180deg,#e8e6e1 0%,#b48e72 50%,#2e2a28 100%)"></div>
    <p class="eyebrow abs" style="left:371px;top:818px">About Me</p>
    <h2 class="heading about-name">Dr. June Tillard</h2>
    <p class="about-role">Owner, Licensed Clinical Psychologist</p>
    <p class="about-text">I earned my Doctor of Psychology (Psy.D.) in Clinical Psychology from Harwood University of Maryland. In addition to my private practice in West Linden Falls, MD, I am also the Director of Counseling at the St. Alden University of Maryland, where I oversee all aspects of counseling services, including outreach programming, crisis intervention, individual and group psychotherapy, as well as consultation with parents, faculty, and staff.</p>
    <a class="btn" href="#" style="left:374px;top:1161px;width:155px;height:53px">Read More</a>
  </section>

  <section class="services">
    <p class="eyebrow abs" style="left:0;top:62px;width:100%;text-align:center">What We Offers</p>
    <h2 class="heading abs" style="left:0;top:96px;width:100%;text-align:center;font-size:46px">Our Services</h2>
    <svg class="arrow" style="left:1140px;top:378px" viewBox="0 0 22 30"><path d="M16 4 L6 15 L16 26" fill="none" stroke="#3d3a38" stroke-width="2"/></svg>
    <svg class="arrow" style="left:1140px;top:424px" viewBox="0 0 22 30"><path d="M6 4 L16 15 L6 26" fill="none" stroke="#c8897a" stroke-width="2"/></svg>
  </section>
  <article class="card" style="left:75px">
    <div class="photo arch" role="img" aria-label="Client talking with a therapist on a sofa" style="background:linear-gradient(180deg,#e4e0da 0%,#a7a4a8 55%,#4e5568 100%)"></div>
    <h3>Individual Therapy</h3>
    <p>Sed ut perspiciatis unde omnis iste natus error sit voluptatem accusantium doloremque laudantium.</p>
    <a class="btn" href="#">Read More</a>
  </article>
  <article class="card" style="left:438px">
    <div class="photo arch" role="img" aria-label="Smiling couple seated together on a couch" style="background:linear-gradient(180deg,#ebe9e5 0%,#b7c2cf 55%,#7c8794 100%)"></div>
    <h3>Couples Therapy</h3>
    <p>Sed ut perspiciatis unde omnis iste natus error sit voluptatem accusantium doloremque laudantium.</p>
    <a class="btn" href="#">Read More</a>
  </article>
  <article class="card" style="left:798px">
    <div class="photo arch" role="img" aria-label="Parents and child sitting together at home" style="background:linear-gradient(180deg,#e6e4df 0%,#a9aab0 55%,#5f6470 100%)"></div>
    <h3>Family Counseling</h3>
    <p>Sed ut perspiciatis unde omnis iste natus error sit voluptatem accusantium doloremque laudantium.</p>
    <a class="btn" href="#">Read More</a>
  </article>

  <section class="issues">
    <h2 class="heading issues-title">Are you struggling with issues<br>that affect the way you live,<br>love or work?</h2>
    <p class="issues-intro">Dr. June Tillard and her associates are licensed psychologists in Linden Falls, Maryland. We offer therapy for individuals, couples and families to help you create meaningful change, whether you:</p>
    <ul class="checklist">
      <li><svg viewBox="0 0 12 12"><circle cx="6" cy="6" r="6" fill="#c8897a"/><path d="M3.2 6.2 L5.2 8 L8.8 4.2" fill="none" stroke="#fff" stroke-width="1.4"/></svg>Feel overwhelmed with depression or anxiety.</li>
      <li><svg viewBox="0 0 12 12"><circle cx="6" cy="6" r="6" fill="#c8897a"/><path d="M3.2 6.2 L5.2 8 L8.8 4.2" fill="none" stroke="#fff" stroke-width="1.4"/></svg>Experience a lack of connection in your marriage.</li>
      <li><svg viewBox="0 0 12 12"><circle cx="6" cy="6" r="6" fill="#c8897a"/><path d="M3.2 6.2 L5.2 8 L8.8 4.2" fill="none" stroke="#fff" stroke-width="1.4"/></svg>Worry excessively about what others think.</li>
      <li><svg viewBox="0 0 12 12"><circle cx="6" cy="6" r="6" fill="#c8897a"/><path d="M3.2 6.2 L5.2 8 L8.8 4.2" fill="none" stroke="#fff" stroke-width="1.4"/></svg>Have a history of trauma or abuse.</li>
      <li><svg viewBox="0 0 12 12"><circle cx="6" cy="6" r="6" fill="#c8897a"/><path d="M3.2 6.2 L5.2 8 L8.8 4.2" fill="none" stroke="#fff" stroke-width="1.4"/></svg>Parent a child with complex needs.</li>
      <li><svg viewBox="0 0 12 12"><circle cx="6" cy="6" r="6" fill="#c8897a"/><path d="M3.2 6.2 L5.2 8 L8.8 4.2" fill="none" stroke="#fff" stroke-width="1.4"/></svg>Struggle with other life challenges.</li>
    </ul>
    <a class="btn" href="#" style="left:75px;top:2506px;width:155px;height:52px">Read More</a>
    <div class="photo arch" role="img" aria-label="Thoughtful older woman resting her chin on her hands" style="left:798px;top:2100px;width:329px;height:461px;background:linear-gradient(180deg,#eeeae6 0%,#e2c7bd 50%,#c9a79a 100%)"></div>
  </section>

  <section class="partnership">
    <h2 class="heading">Therapy is a Partnership</h2>
    <p>Our clinicians utilize contemporary neuroscience-informed therapies along with the wisdom of traditional psychotherapy to foster insight, mindfulness, self-compassion, and deeper connections to oneself and others. Together, in a safe and non-judgmental environment, we will work to understand what holds you back from living the life you really want. All are welcome and celebrated.</p>
    <a class="btn" href="#" style="left:523px;top:280px;width:155px;height:53px">Read More</a>
  </section>

  <section class="blog">
    <h2 class="heading blog-title">Blog Posts</h2>
    <svg class="arrow" style="left:330px;top:3146px" viewBox="0 0 22 30"><path d="M16 4 L6 15 L16 26" fill="none" stroke="#3d3a38" stroke-width="2"/></svg>
    <svg class="arrow" style="left:370px;top:3146px" viewBox="0 0 22 30"><path d="M6 4 L16 15 L6 26" fill="none" stroke="#c8897a" stroke-width="2"/></svg>
    <article class="post" style="left:75px">
      <div class="photo" role="img" aria-label="Couple talking on a bench outdoors" style="background:linear-gradient(180deg,#c9744f 0%,#e2d2c2 50%,#6f8db0 100%)"></div>
      <h3>Communication in Relationships: Getting to the Heart of the Issue</h3>
      <a href="#">Read More</a>
    </article>
    <article class="post" style="left:438px">
      <div class="photo" role="img" aria-label="Man and woman in a serious conversation at home" style="background:linear-gradient(180deg,#d9cdbf 0%,#b56a3e 50%,#4c4540 100%)"></div>
      <h3>Communication in Relationships: Getting to the Heart of the Issue</h3>
      <a href="#">Read More</a>
    </article>
    <article class="post" style="left:798px">
      <div class="photo" role="img" aria-label="Two women talking in a session room" style="background:linear-gradient(180deg,#b8573c 0%,#9a8c84 50%,#3f4d66 100%)"></div>
      <h3>Communication in Relationships: Getting to the Heart of the Issue</h3>
      <a href="#">Read More</a>
    </article>
  </section>

  <footer class="site-footer">
    <div class="f-col" style="left:75px">
      <h4>Quick Links</h4>
      <a href="#">Welcome</a><a href="#">Services</a><a href="#">About</a><a href="#">FAQs</a><a href="#">Blog</a><a href="#">Contact</a>
    </div>
    <div class="f-col" style="left:331px">
      <h4>Services</h4>
      <a href="#">Individual Therapy</a><a href="#">Couples Therapy</a><a href="#">Family Counseling</a>
    </div>
    <div class="f-col" style="left:593px">
      <h4>Contact</h4>
      <span class="contact-row"><svg viewBox="0 0 14 14"><path d="M3 1 L5.5 1 L6.5 4 L5 5.2 C5.8 7 7 8.2 8.8 9 L10 7.5 L13 8.5 L13 11 C13 12 12 13 11 13 C5.5 12.5 1.5 8.5 1 3 C1 2 2 1 3 1 Z" fill="#fff"/></svg>(555) 014-2290</span>
      <span class="contact-row"><svg viewBox="0 0 14 14"><rect x="1" y="3" width="12" height="9" fill="#fff"/><path d="M1 3.5 L7 8 L13 3.5" fill="none" stroke="#c68d74" stroke-width="1.2"/></svg>hello@junetillard.com</span>
    </div>
    <div class="social" aria-label="Social profiles"><span></span><span class="on"></span><span></span><span></span><span></span></div>
    <div class="f-col" style="left:885px"><h4>Email Subscribe</h4></div>
    <div class="email-input">Enter Email</div>
    <a class="btn subscribe" href="#">Subscribe</a>
    <div class="f-rule"></div>
    <p class="copyright">Copyright © 2024 June S. Tillard, Psy.D. All Right Reserved</p>
  </footer>

</div>
</body>
</html>
```